Honesty box for charity and people with disabilities

Please design an honesty box that stands out and makes people want to help. include the following
* we have been in business since 2007
* we employ people with disabilities
* we support Australian based charities
* all items are $2.60 each
*Thank you for choosing to support our box.

By supporting Moth’s Lantern you are insuring your valued money is going to make a real difference!!!

Real jobs for people with Disabilities

Real support for Australian Charities.

The Honesty Box that Honestly makes a difference!!!

* would like to change logo a bit. Open to ideas but would like to keep the bee.

* also would look at different wording. You can visit our website to get an idea of what we do. www.mothslanternhub.com.au

*for a refill or more information please visit www.mothslanternhub.com.au we have 2 types of boxes a yellow box and a bigger box it is the bigger box on the website that we need art work for not the yellow one

Also under supporting Australian charities need to put see website for charities we support.

Target Market(s)

18-60 years old

Industry/Entity Type

Business

Logo Text

Moth's Lantern

Font styles to use
Sans Serif

Colors
0255a3
ec1f27
fbed22
1b1b1b

Requirements
Must have
• wording of what we do must stand out that we employe people with disabilities.
• Make it priority
Nice to have
• A nice colourful box
Should not have
• Moth's Lantern lollie tray file this is an old box design please disregard the art work on the box
• The box should not look anything like the old box in the picture I only posted this for the box dimensions

```html
<!DOCTYPE html>
<html lang="en">
<head>
<meta charset="utf-8">
<title>Moth's Lantern Honesty Box – Dieline</title>
<link rel="stylesheet" href="https://fonts.googleapis.com/css2?family=Roboto:ital,wght@0,400;0,500;0,700;0,900;1,400&family=Oswald:wght@700&display=swap">
<style>
  :root{
    --blue:#0255a3;
    --blue-light:#1a78d6;
    --blue-dark:#0b3f78;
    --red:#ec1f27;
    --gold:#fbbf2f;
    --gold-dark:#f0a81c;
    --ink:#1b1b1b;
    --white:#ffffff;
  }
  html,body{margin:0;padding:0;overflow:hidden;background:var(--white)}
  .dieline{position:relative;width:1150px;height:1200px;overflow:hidden;background:var(--white);font-family:"Roboto",sans-serif}

  /* ---------- flaps ---------- */
  .flap{position:absolute;background:var(--blue);transform-origin:center center}
  .flap--bottom{left:312.5px;top:962px;width:530px;height:110.5px;--badge-x:62px;--notice-x:116px;--notice-w:300px}
  .flap--top{left:312.5px;top:196px;width:530px;height:110.5px;transform:rotate(180deg);--badge-x:62px;--notice-x:116px;--notice-w:300px}
  .flap--left{left:-69px;top:580px;width:655px;height:108px;transform:rotate(90deg);--badge-x:96px;--notice-x:177px;--notice-w:303px}
  .flap--right{left:570px;top:578.5px;width:655px;height:111px;transform:rotate(-90deg);--badge-x:96px;--notice-x:177px;--notice-w:303px}

  .flap__badge{position:absolute;top:50%;left:var(--badge-x);width:96px;height:96px;transform:translate(-50%,-50%)}
  .flap__notice{position:absolute;top:50%;left:var(--notice-x);width:var(--notice-w);height:54px;transform:translateY(-50%);
    box-sizing:border-box;border:1.5px dashed var(--white);display:flex;align-items:center;justify-content:center;text-align:center;
    color:var(--white);font:700 12px/1.4 "Roboto",sans-serif;text-transform:uppercase}
  .flap__info{position:absolute;right:0;top:0;width:108px;height:100%;background:var(--gold);box-sizing:border-box;padding:12px 4px 6px;
    text-align:center;color:var(--white)}
  .info__name{font:700 11px/1.05 "Roboto",sans-serif;text-transform:uppercase;white-space:nowrap}
  .info__ltd{font:500 9px/1.3 "Roboto",sans-serif;letter-spacing:4px}
  .info__label{font:400 5px/1.2 "Roboto",sans-serif;letter-spacing:2px;color:var(--ink);margin-top:3px}
  .info__phone{font:700 12.5px/1.1 "Roboto",sans-serif;color:var(--ink)}
  .info__web{font:500 5.6px/1.2 "Roboto",sans-serif;color:var(--ink)}

  /* ---------- price badge (themable via inherited variables) ---------- */
  .price-badge{--badge-fill:var(--gold);--badge-frame:var(--gold);--badge-dash:var(--gold);--badge-accent:var(--ink)}
  .price-badge--main{--badge-fill:var(--ink);--badge-frame:var(--gold);--badge-dash:var(--red);--badge-accent:var(--gold)}
  .badge__frame{fill:none;stroke:var(--badge-frame);stroke-width:2}
  .badge__fill{fill:var(--badge-fill)}
  .badge__dash{fill:none;stroke:var(--badge-dash);stroke-width:1.2;stroke-dasharray:3 3}
  .badge__small{font:500 4.6px "Roboto",sans-serif;fill:var(--badge-accent)}
  .badge__price{font:700 20px "Oswald",sans-serif;fill:var(--white)}
  .badge__each{font:700 8.5px "Oswald",sans-serif;fill:var(--badge-accent);letter-spacing:3px}

  /* ---------- front panel ---------- */
  .front{position:absolute;left:312.5px;top:306.5px;width:529.5px;height:655.5px;background:var(--red);overflow:hidden}
  .front__mark{position:absolute;left:200px;top:41px;width:124px;height:124px;border-radius:50%;background:var(--gold)}
  .front__ribbons{position:absolute;left:0;top:0;width:529.5px;height:460px}
  .front__title{position:absolute;left:79px;top:191px;width:368px;height:54px;margin:0;display:flex;align-items:center;justify-content:center;
    white-space:nowrap;color:var(--white);font:500 32px/1 "Roboto",sans-serif;letter-spacing:2px;text-transform:uppercase}
  .claim{position:absolute;margin:0;font:500 16.5px/1.3 "Roboto",sans-serif;color:var(--white);white-space:nowrap}
  .claim--yellow{left:76px;top:279px}
  .claim--blue{left:18px;top:352px;width:355px;text-align:center}
  .front__price{position:absolute;left:385px;top:272px;width:108px;height:108px}
  .front__price-shadow{position:absolute;left:405px;top:380px;width:80px;height:8px;border-radius:50%;background:rgba(120,10,10,.35);filter:blur(3px)}

  .front__band{position:absolute;left:0;top:473px;width:100%;height:108.5px;background:var(--ink)}
  .benefits{position:absolute;left:22px;top:484px;margin:0;padding:0;list-style:none;width:320px}
  .benefits li{position:relative;padding-left:18px;font:italic 400 10px/1.4 "Roboto",sans-serif;color:var(--white);margin-bottom:7px}
  .benefits li::before{content:"";position:absolute;left:0;top:1px;width:9px;height:9px;border-radius:50%;background:var(--red);box-shadow:0 0 0 1.5px var(--white)}

  .front__brand{position:absolute;left:359px;top:460px;width:118px;height:118px;border-radius:50%;background:var(--gold);
    display:flex;align-items:center;justify-content:center;text-align:center;color:var(--ink);font:700 15px/1.15 "Roboto",sans-serif;text-transform:uppercase}
  .front__visit{position:absolute;left:22.5px;top:596px}
  .front__visit-label{font:700 8px/1 "Roboto",sans-serif;color:var(--ink);text-transform:uppercase;margin-bottom:7px}
  .front__visit-url{font:400 8.5px/1 "Roboto",sans-serif;letter-spacing:.3px;color:var(--white)}
</style>
</head>
<body>
<div class="dieline">

  <svg width="0" height="0" style="position:absolute">
    <defs>
      <g id="price-badge">
        <polygon class="badge__dash" points="62,10 92,38 86,80 40,92"/>
        <polygon class="badge__frame" points="50,3 97,50 50,97 3,50"/>
        <polygon class="badge__fill" points="50,10 90,50 50,90 10,50"/>
        <text class="badge__small" x="50" y="40" text-anchor="middle">ALL ITEMS ARE</text>
        <text class="badge__price" x="50" y="59" text-anchor="middle">$2.60</text>
        <text class="badge__each" x="51.5" y="70" text-anchor="middle">EACH</text>
      </g>
    </defs>
  </svg>

  <!-- flaps -->
  <section class="flap flap--top">
    <svg class="flap__badge price-badge" viewBox="0 0 100 100"><use href="#price-badge"/></svg>
    <div class="flap__notice">We give upto 5 times more to other charity<br>thensome other honesty boxes</div>
    <div class="flap__info">
      <div class="info__name">Moth's Lantern<br>Australia</div>
      <div class="info__ltd">PTY LTD</div>
      <div class="info__label">PHONE</div>
      <div class="info__phone">0491 570 156</div>
      <div class="info__label">WEBSITE</div>
      <div class="info__web">www.mothslanternhub.com.au</div>
    </div>
  </section>

  <section class="flap flap--left">
    <svg class="flap__badge price-badge" viewBox="0 0 100 100"><use href="#price-badge"/></svg>
    <div class="flap__notice">We give upto 5 times more to other charity<br>thensome other honesty boxes</div>
    <div class="flap__info">
      <div class="info__name">Moth's Lantern<br>Australia</div>
      <div class="info__ltd">PTY LTD</div>
      <div class="info__label">PHONE</div>
      <div class="info__phone">0491 570 156</div>
      <div class="info__label">WEBSITE</div>
      <div class="info__web">www.mothslanternhub.com.au</div>
    </div>
  </section>

  <section class="flap flap--right">
    <svg class="flap__badge price-badge" viewBox="0 0 100 100"><use href="#price-badge"/></svg>
    <div class="flap__notice">We give upto 5 times more to other charity<br>thensome other honesty boxes</div>
    <div class="flap__info">
      <div class="info__name">Moth's Lantern<br>Australia</div>
      <div class="info__ltd">PTY LTD</div>
      <div class="info__label">PHONE</div>
      <div class="info__phone">0491 570 156</div>
      <div class="info__label">WEBSITE</div>
      <div class="info__web">www.mothslanternhub.com.au</div>
    </div>
  </section>

  <section class="flap flap--bottom">
    <svg class="flap__badge price-badge" viewBox="0 0 100 100"><use href="#price-badge"/></svg>
    <div class="flap__notice">We give upto 5 times more to other charity<br>thensome other honesty boxes</div>
    <div class="flap__info">
      <div class="info__name">Moth's Lantern<br>Australia</div>
      <div class="info__ltd">PTY LTD</div>
      <div class="info__label">PHONE</div>
      <div class="info__phone">0491 570 156</div>
      <div class="info__label">WEBSITE</div>
      <div class="info__web">www.mothslanternhub.com.au</div>
    </div>
  </section>

  <!-- front panel -->
  <main class="front">
    <div class="front__mark" role="img" aria-label="Brand emblem area"></div>

    <svg class="front__ribbons" viewBox="0 0 529.5 460">
      <polygon fill="#1b1b1b" points="79,191 447,191 432,218 447,245 79,245 94,218"/>
      <polygon fill="#f0a81c" points="124,245 209,245 209,268 124,268"/>
      <polygon fill="#1a78d6" points="288,318 355,318 355,342 288,342"/>
      <polygon fill="#fbbf2f" points="64,268 378,262 378,327 64,334"/>
      <polygon fill="#1a78d6" points="88,394 175,400 175,412 100,408"/>
      <polygon fill="#0b3f78" points="175,400 245,398 245,412 175,412"/>
      <polygon fill="#1a78d6" points="88,394 108,408 108,442 88,420"/>
      <polygon fill="#0255a3" points="18,342 373.5,345 373.5,405 18,398"/>
    </svg>

    <h1 class="front__title">Moth's Lantern</h1>
    <p class="claim claim--yellow">We have been in business since 2007<br>We employ people with disabilities</p>
    <p class="claim claim--blue">We support Australian based charities<br>Thank you for choosing to support our box.</p>

    <div class="front__price-shadow"></div>
    <svg class="front__price price-badge price-badge--main" viewBox="0 0 100 100"><use href="#price-badge"/></svg>

    <div class="front__band"></div>
    <ul class="benefits">
      <li>By supporting Moth’s Lantern you are insuring your valued money is going to make a real difference!!!</li>
      <li>Real jobs for people with Disabilities</li>
      <li>Real support for Australian Charities.</li>
      <li>The Honesty Box that Honestly makes a difference!!!</li>
    </ul>

    <div class="front__brand">Moth's<br>Lantern</div>

    <div class="front__visit">
      <div class="front__visit-label">Visit our website</div>
      <div class="front__visit-url">HTTP://WWW.MOTHSLANTERNHUB.COM.AU</div>
    </div>
  </main>

</div>
</body>
</html>
```